Create a memorable Stationary for Security Software Company

TelVandrik is the worldwide leader in securing the Internet. Making Internet communications and critical data secure, reliable and available everywhere has been and continues to be our ongoing vision. We are committed to staying focused on real customer needs and to developing new and innovative security solutions that redefine the security landscape.

Industry/Entity Type

Internet

Font styles to use
Serif
Sans Serif
Script

Colors
0792cd
33a6d7
85cae6

```html
<!DOCTYPE html>
<html lang="en">
<head>
<meta charset="utf-8">
<title>TelVandrik Business Card</title>
<link rel="stylesheet" href="https://fonts.googleapis.com/css2?family=Arimo:wght@400;700&display=swap">
<style>
  :root {
    --brand-deep: #0792cd;
    --brand-mid: #33a6d7;
    --brand-light: #85cae6;
    --brand-pale: #b5e0f2;
    --brand-navy: #0a5f8f;
    --ink-white: #ffffff;
    --page-bg: #e9eef1;
  }
  * { margin: 0; padding: 0; box-sizing: border-box; }
  html, body { width: 1200px; height: 950px; overflow: hidden; }
  body {
    background: var(--page-bg);
    font-family: "Arimo", Arial, sans-serif;
    position: relative;
  }
  .card {
    position: absolute;
    left: 250px;
    width: 700px;
    height: 400px;
    overflow: hidden;
    box-shadow: 0 6px 18px rgba(0, 40, 70, 0.18);
  }
  .card-back {
    top: 50px;
    background: linear-gradient(135deg, var(--brand-deep) 0%, #0a7fb8 55%, var(--brand-navy) 100%);
  }
  .card-front { top: 500px; }

  /* back */
  .back-mark {
    position: absolute;
    left: 0; right: 0; top: 150px;
    display: flex; align-items: center; justify-content: center; gap: 16px;
  }
  .back-mark .mark-dot {
    width: 46px; height: 46px; border-radius: 50%;
    background: rgba(133, 202, 230, 0.35);
  }
  .back-mark .mark-name {
    font-weight: 700; font-size: 46px;
    color: rgba(133, 202, 230, 0.45);
  }
  .back-web {
    position: absolute; left: 0; right: 0; top: 232px;
    text-align: center; font-size: 17px; letter-spacing: 2px;
    color: rgba(133, 202, 230, 0.45);
  }

  /* front */
  .front-art { position: absolute; inset: 0; }
  .front-mark {
    position: absolute; left: 48px; top: 58px;
    display: flex; align-items: center; gap: 12px;
  }
  .front-mark .mark-dot {
    width: 36px; height: 36px; border-radius: 50%;
    background: var(--brand-deep);
  }
  .front-mark .mark-name {
    font-weight: 700; font-size: 34px; color: var(--brand-deep);
  }
  .contact {
    position: absolute; right: 34px; top: 150px;
    text-align: right; color: var(--ink-white);
  }
  .contact-name { font-weight: 700; font-size: 20px; line-height: 24px; letter-spacing: 0.5px; }
  .contact-role { font-size: 16px; line-height: 20px; letter-spacing: 0.5px; margin-bottom: 10px; }
  .contact-address { font-size: 15px; line-height: 20px; margin-bottom: 10px; }
  .contact-line {
    display: flex; justify-content: flex-end; align-items: center; gap: 8px;
    font-size: 15px; line-height: 22px;
  }
  .contact-line svg { width: 15px; height: 15px; fill: var(--ink-white); }
</style>
</head>
<body>

<section class="card card-back">
  <div class="back-mark">
    <span class="mark-dot"></span>
    <span class="mark-name">TelVandrik</span>
  </div>
  <div class="back-web">www.telvandrik.com</div>
</section>

<section class="card card-front">
  <svg class="front-art" viewBox="0 0 700 400" preserveAspectRatio="none">
    <defs>
      <linearGradient id="front-sky" x1="0" y1="0" x2="1" y2="1">
        <stop offset="0" stop-color="#c4e7f5"/>
        <stop offset="1" stop-color="#85cae6"/>
      </linearGradient>
      <linearGradient id="front-sea" x1="0" y1="0" x2="1" y2="1">
        <stop offset="0" stop-color="#33a6d7"/>
        <stop offset="0.5" stop-color="#0792cd"/>
        <stop offset="1" stop-color="#0a6fa5"/>
      </linearGradient>
    </defs>
    <rect width="700" height="400" fill="url(#front-sky)"/>
    <path d="M0 205 C140 300 260 300 380 225 C500 140 600 55 700 48 L700 400 L0 400 Z" fill="#5bb8df"/>
    <path d="M0 240 C140 330 260 325 380 258 C500 175 600 95 700 85 L700 400 L0 400 Z" fill="url(#front-sea)"/>
    <path d="M0 225 C140 315 260 312 380 242 C500 158 600 75 700 66" fill="none" stroke="#ffffff" stroke-width="3"/>
    <path d="M0 268 C150 345 280 345 420 282" fill="none" stroke="#ffffff" stroke-opacity="0.5" stroke-width="2"/>
  </svg>

  <div class="front-mark">
    <span class="mark-dot"></span>
    <span class="mark-name">TelVandrik</span>
  </div>

  <div class="contact">
    <div class="contact-name">MARA ELLISON</div>
    <div class="contact-role">PRESIDENT</div>
    <div class="contact-address">2716 Harbor Crest Lane<br>Elm Ridge, NY 11420</div>
    <div class="contact-line">555 0142 7781
      <svg viewBox="0 0 16 16"><path d="M2 5c0-2 2-3 6-3s6 1 6 3v1h-3V5H5v1H2z M4 7h8l2 6H2z"/></svg>
    </div>
    <div class="contact-line">555 0193 4620
      <svg viewBox="0 0 16 16"><path d="M4 1h8v4H4z M1 6h14v6h-2v-2H3v2H1z M4 11h8v4H4z"/></svg>
    </div>
    <div class="contact-line">mara@telvandrik.com
      <svg viewBox="0 0 16 16"><path d="M1 3h14v1L8 9 1 4z M1 6l7 5 7-5v7H1z"/></svg>
    </div>
    <div class="contact-line">www.telvandrik.com
      <svg viewBox="0 0 16 16"><circle cx="8" cy="8" r="7"/><path d="M1 8h14 M8 1c-3 4-3 10 0 14 M8 1c3 4 3 10 0 14" stroke="#0792cd" stroke-width="1" fill="none"/></svg>
    </div>
  </div>
</section>

</body>
</html>
```